Fernly Garage Doors Business Card

I need a Business Card for my garage door business:
Fernly Garage Doors.
please add:
logo
phone number: 833-2-FERNLY
(337-659)

email: service@fernlygaragedoors.com
website: www.fernlygaragedoors.com

The attached image is recommendation ONLY.

```html
<!DOCTYPE html>
<html lang="en">
<head>
<meta charset="utf-8">
<title>Fernly Garage Doors – Business Card</title>
<link rel="stylesheet" href="https://fonts.googleapis.com/css2?family=Open+Sans:wght@400;600&display=swap">
<style>
  :root {
    --stage: #2d2d2d;
    --teal: #80d8df;
    --paper: #ffffff;
    --ink: #111111;
    --rule: #222222;
  }
  * { box-sizing: border-box; margin: 0; padding: 0; }
  html, body { width: 1200px; height: 1166px; overflow: hidden; }
  body {
    background: var(--stage);
    font-family: "Open Sans", sans-serif;
    color: var(--ink);
    position: relative;
  }
  .card {
    position: absolute;
    left: 250px;
    width: 700px;
    height: 400px;
    overflow: hidden;
    box-shadow: 0 14px 30px rgba(0,0,0,0.45);
  }
  .card--front { top: 150px; background: var(--teal); }
  .card--back { top: 616px; background: var(--paper); }

  .brand {
    position: absolute;
    display: flex;
    align-items: center;
    gap: 22px;
  }
  .brand__dot {
    width: 84px; height: 84px;
    border-radius: 50%;
    flex: none;
  }
  .brand__name {
    font-weight: 600;
    font-size: 42px;
    line-height: 1.05;
    color: var(--ink);
  }
  .card--front .brand { left: 150px; top: 140px; }
  .card--front .brand__dot { background: var(--paper); }
  .front__web {
    position: absolute;
    left: 0; right: 0; bottom: 46px;
    text-align: center;
    font-size: 15px;
    letter-spacing: 3px;
  }

  .card--back .brand { left: 250px; top: 40px; }
  .card--back .brand__dot { background: var(--teal); width: 74px; height: 74px; }
  .card--back .brand__name { font-size: 34px; }

  .rule-top {
    position: absolute; left: 330px; right: 40px; top: 150px;
    height: 1px; background: var(--rule);
  }
  .rule-mid {
    position: absolute; left: 40px; right: 40px; top: 252px;
    height: 1px; background: var(--rule);
  }
  .person { position: absolute; left: 40px; top: 185px; }
  .person__name { font-size: 26px; font-weight: 400; line-height: 1.1; }
  .person__role { font-size: 20px; color: var(--teal); line-height: 1.2; }

  .phone {
    position: absolute; right: 40px; top: 172px;
    display: flex; align-items: center; gap: 10px;
    font-size: 19px;
  }
  .contacts {
    position: absolute; left: 40px; top: 272px;
    list-style: none;
    font-size: 19px;
  }
  .contacts li { display: flex; align-items: center; gap: 14px; line-height: 32px; }
  .icon { width: 20px; height: 20px; flex: none; }
  .band {
    position: absolute; left: 0; right: 0; bottom: 0;
    height: 22px; background: var(--teal);
  }
</style>
</head>
<body>
  <section class="card card--front" aria-label="Business card front">
    <div class="brand">
      <span class="brand__dot"></span>
      <span class="brand__name">Fernly<br>Garage Doors</span>
    </div>
    <p class="front__web">www.fernlygaragedoors.com</p>
  </section>

  <section class="card card--back" aria-label="Business card back">
    <div class="brand">
      <span class="brand__dot"></span>
      <span class="brand__name">Fernly<br>Garage Doors</span>
    </div>
    <div class="rule-top"></div>

    <div class="phone">
      <svg class="icon" viewBox="0 0 24 24"><path fill="#80d8df" d="M6.6 10.8a15 15 0 0 0 6.6 6.6l2.2-2.2c.3-.3.7-.4 1-.2 1.1.4 2.3.6 3.6.6.6 0 1 .4 1 1V20c0 .6-.4 1-1 1A17 17 0 0 1 3 4c0-.6.4-1 1-1h3.5c.6 0 1 .4 1 1 0 1.3.2 2.5.6 3.6.1.3 0 .7-.2 1z"/></svg>
      <span>833-2-FERNLY (337-659)</span>
    </div>

    <div class="person">
      <p class="person__name">Marcus Bellamy</p>
      <p class="person__role">Manager</p>
    </div>
    <div class="rule-mid"></div>

    <ul class="contacts">
      <li>
        <svg class="icon" viewBox="0 0 24 24"><rect x="2" y="5" width="20" height="14" fill="#80d8df"/><path d="M2 5l10 8 10-8" fill="none" stroke="#fff" stroke-width="1.6"/></svg>
        <span>service@fernlygaragedoors.com</span>
      </li>
      <li>
        <svg class="icon" viewBox="0 0 24 24" fill="none" stroke="#80d8df" stroke-width="1.8"><circle cx="12" cy="12" r="9.5"/><ellipse cx="12" cy="12" rx="4" ry="9.5"/><path d="M2.5 12h19M4 7h16M4 17h16"/></svg>
        <span>www.fernlygaragedoors.com</span>
      </li>
    </ul>
    <div class="band"></div>
  </section>
</body>
</html>
```